MOON BITES CANDY MYLAR BAG FILE SET UP FOR PRINT

☆6 FLAVORS
(It's ok to set up 1 flavor until the design is set then doing the rest of the flavors if it is easier)*
GREEN BAG
LYNX DRIFT
WATERMELON
PINK BAG
STRAWBERRY LEMONADE
PURPLE BAG
RIVER PLUM
LIGHT BLUE BAG
DA DA MANGO
BLUE BAG
KOBO ZING
☆Please Use the template (4"x6") , it is the correct size we need for the design.
INFORMATION FOR THE LABEL below
:::::
The FRONT/ BACK should be set up the same, any changes are below ::
THC
SUGAR
DROPS
SWEET & DELICIOUS MOON FIZZ BITES WITH MOUTHWATERING FLAVOR AND THC
10 PIECES PER PACKAGE - 200 MG THC TOTAL
on the back I need a small square candy with rounded corners with a dotted line down the middle . The candy should be about 1/4th the size of the taffy piece on the attached mylar)
10 MG THC = 1/2 PIECE
INGREDIENTS : CANE SUGAR, CONFECTIONERS GLUCOSE, WATER, THC EXTRACT, NATURAL & ARTIFICIAL FLAVORS & COLORS
ALLERGEN WARNING : MADE IN A FACILITY THAT HANDLES PEANUTS AND OTHER TREE NUTS.

```html
<!DOCTYPE html>
<html lang="en">
<head>
<meta charset="utf-8">
<title>Moon Bites – Blue Punch Mylar Bag</title>
<link rel="stylesheet" href="https://fonts.googleapis.com/css2?family=Fredoka:wght@600;700&family=Open+Sans:wght@600;700;800&display=swap">
<style>
  :root{
    --bag:#bfe0f6;
    --white:#ffffff;
    --glow:#5ba7e3;
    --die:#1d9a72;
    --ink:#1e4c86;
    --badge:#1f8f3a;
    --candy-a:#7fd3e6;
    --candy-b:#2fa8c8;
  }
  *{margin:0;padding:0;box-sizing:border-box}
  html,body{width:1200px;height:4096px;overflow:hidden;background:var(--bag)}
  .bag{position:relative;width:1200px;height:4096px;background:var(--bag);overflow:hidden}
  .dieline{position:absolute;inset:0}
  .display{position:absolute;left:0;width:1200px;text-align:center;color:var(--white);
    font-family:"Fredoka",sans-serif;font-weight:700;line-height:1;
    text-shadow:0 0 18px var(--glow),0 0 6px var(--glow)}
  .headline{font-size:200px;letter-spacing:2px}
  .flavor{font-size:112px}
  .tagline{position:absolute;left:0;width:1200px;text-align:center;color:var(--white);
    font-family:"Open Sans",sans-serif;font-weight:800;font-size:33px;line-height:46px}
  .net{position:absolute;left:0;width:1200px;text-align:center;color:var(--white);
    font-family:"Open Sans",sans-serif;font-weight:800;font-size:30px}
  .brand{position:absolute;left:0;width:1200px;text-align:center;color:var(--white);
    font-family:"Fredoka",sans-serif;font-weight:700;line-height:.95}
  .badge{position:absolute;left:928px;top:380px;width:160px;height:160px;background:var(--badge);border-radius:14px}

  .back{position:absolute;left:80px;top:2440px;width:1040px;height:1460px;transform:rotate(180deg);
    color:var(--ink);font-family:"Open Sans",sans-serif;font-weight:700;font-size:26px;line-height:34px;
    padding:60px 40px 40px}
  .dose-row{display:flex;justify-content:space-between;align-items:flex-start;margin-bottom:20px}
  .dose{width:400px}
  .dose-label{font-weight:800;font-size:28px;margin-bottom:16px}
  .pieces{display:flex;border:3px solid var(--ink);height:78px;width:400px}
  .pieces span{flex:1;border-right:3px solid var(--ink);display:flex;align-items:center;justify-content:center;font-size:28px}
  .pieces span:last-child{border-right:none}
  .candy{width:250px;height:270px;margin-right:80px;border-radius:28px;
    background:linear-gradient(160deg,var(--candy-a),var(--candy-b))}
  .facts{width:640px;margin-top:-150px}
  .facts p{margin-bottom:8px}
  .block{margin-top:16px}
  .boxed{border:3px solid var(--ink);padding:12px 18px;margin-top:18px}
  .made{font-size:34px;font-weight:800;margin-top:26px}
  .sign-off{display:flex;justify-content:space-between;align-items:flex-end;margin-top:24px}
  .back-brand{font-family:"Fredoka",sans-serif;font-weight:700;font-size:78px;line-height:.95;text-align:center}
  .company{text-align:left;font-size:26px;line-height:34px}
</style>
</head>
<body>
<div class="bag">
  <svg class="dieline" width="1200" height="4096" viewBox="0 0 1200 4096" fill="none">
    <circle cx="600" cy="48" r="18" stroke="var(--die)" stroke-width="4"/>
    <circle cx="600" cy="4046" r="18" stroke="var(--die)" stroke-width="4"/>
    <line x1="0" y1="120" x2="1200" y2="120" stroke="var(--die)" stroke-width="4"/>
    <line x1="0" y1="176" x2="1200" y2="176" stroke="var(--die)" stroke-width="3" stroke-dasharray="14 10"/>
    <line x1="0" y1="3960" x2="1200" y2="3960" stroke="var(--die)" stroke-width="4"/>
    <line x1="0" y1="3916" x2="1200" y2="3916" stroke="var(--die)" stroke-width="3" stroke-dasharray="14 10"/>
    <rect x="32" y="120" width="1136" height="1560" rx="48" stroke="var(--die)" stroke-width="4"/>
    <rect x="32" y="1712" width="1136" height="656" rx="48" stroke="var(--die)" stroke-width="4"/>
    <rect x="32" y="2392" width="1136" height="1568" rx="48" stroke="var(--die)" stroke-width="4"/>
    <rect x="80" y="192" width="1040" height="1440" rx="20" stroke="var(--die)" stroke-width="3" stroke-dasharray="14 10"/>
    <rect x="80" y="1760" width="1040" height="568" rx="20" stroke="var(--die)" stroke-width="3" stroke-dasharray="14 10"/>
    <rect x="80" y="2440" width="1040" height="1460" rx="20" stroke="var(--die)" stroke-width="3" stroke-dasharray="14 10"/>
  </svg>

  <!-- front panel -->
  <div class="badge" role="img" aria-label="Cannabis product badge"></div>
  <div class="display headline" style="top:470px">THC</div>
  <div class="display headline" style="top:645px">MOON</div>
  <div class="display headline" style="top:818px">BITES</div>
  <div class="display flavor" style="top:1018px">BLUE PUNCH</div>
  <p class="tagline" style="top:1172px">SWEET &amp; DELICIOUS MOON FIZZ BITES<br>WITH MOUTHWATERING FLAVOR AND THC</p>
  <div class="brand" style="top:1330px;font-size:104px">TOKE<br>TREATS</div>
  <p class="net" style="top:1572px">10 PIECES PER PACKAGE - 200 MG THC TOTAL</p>

  <!-- gusset / middle panel -->
  <div class="brand" style="top:1880px;font-size:100px">TOKE<br>TREATS</div>
  <div class="display flavor" style="top:2090px">BLUE PUNCH</div>

  <!-- back panel (printed inverted) -->
  <div class="back">
    <div class="dose-row">
      <div class="dose">
        <div class="dose-label">10 MG THC = 1/2 PIECE</div>
        <div class="pieces"><span>1</span><span>2</span><span>3</span><span>4</span><span>5</span><span>6</span><span>7</span><span>8</span><span>9</span><span>10</span></div>
      </div>
      <div class="candy" role="img" aria-label="Square blue candy piece with rounded corners and a dotted line down the middle"></div>
    </div>
    <div class="facts">
      <p>INGREDIENTS : CANE SUGAR,<br>CONFECTIONERS GLUCOSE, WATER,<br>THC EXTRACT, NATURAL &amp; ARTIFICIAL<br>FLAVORS &amp; COLORS</p>
      <p>ALLERGEN WARNING : MADE IN A<br>FACILITY THAT HANDLES PEANUTS<br>AND OTHER TREE NUTS.</p>
    </div>
    <p class="block">WARNING : THIS PRODUCT IS FOR USE BY INDIVIDUALS 21 YRS OF AGE OR OLDER OR BY REGISTERED QUALIFYING PATIENTS ONLY. IT IS ILLEGAL TO DRIVE A MOTOR VEHICLE WHILE UNDER THE INFLUENCE OF MARIJUANA</p>
    <p class="block">KEEP OUT OF REACH OF CHILDREN<br>NATIONAL POISON CONTROL CENTRE 1 800 555 0142</p>
    <p class="boxed">USE BY PREGNANT OR BREASTFEEDING WOMEN OR BY WOMEN PLANNING TO BECOME PREGNANT MAY RESULT IN FETAL INJURY, PRETERM BIRTH, LOW BIRTHWEIGHT OR DEVELOPMENTAL PROBLEMS FOR THE CHILD.</p>
    <p class="block">ACTIVATION TIME | 30 - 45 MINUTES</p>
    <p class="block">THE ACTUAL VALUE OF CANNABINOIDS MAY VARY FROM THE REPORTED VALUE BY +/- 10 %</p>
    <p class="made">MADE IN A MARIJUANA FACILITY</p>
    <div class="sign-off">
      <div class="back-brand">TOKE<br>TREATS</div>
      <p class="company">MIRA'S TOKE COMPANY<br>AU P 000 184<br>WWW.TOKETREATS.SHOP</p>
    </div>
  </div>
</div>
</body>
</html>
```